Create a memorable Web Design for real estate branding

we are a Minnepolis brokerage and boutique housing specialist with over 27 years of experience in the Global furnished housing industry, servicing the Greater Los Angeles area. Specializing in “warm environments” we offer a customized approach to satisfying our guests and client’s needs by offering a wide array of options in highly desirable areas. Additionally, Lanterly Homes Collective offers assistance and expertise to home buyers, sellers and investors.

Industry/Entity Type

Real Estate

Number of Pages Required

1 page

Font styles to use
Serif
Sans Serif
Decorative

```html
<!DOCTYPE html>
<html lang="en">
<head>
<meta charset="utf-8">
<title>Marlowe Vane Real Estate</title>
<link rel="stylesheet" href="https://fonts.googleapis.com/css2?family=Open+Sans:wght@400;600;700&family=Roboto+Condensed:wght@400;700&display=swap">
<style>
:root{
  --teal:#1fb095;
  --teal-dark:#17957e;
  --lime:#8cc63f;
  --ink:#333a3f;
  --muted:#777f85;
  --light:#f1f3f4;
  --line:#dde2e4;
  --white:#fff;
  --black:#111;
}
*{box-sizing:border-box;margin:0;padding:0}
html,body{width:1200px;height:2820px;overflow:hidden}
body{font-family:"Open Sans",sans-serif;color:var(--ink);background:var(--white);position:relative}
.heading{font-family:"Roboto Condensed",sans-serif;font-weight:700}
.site-header{position:absolute;top:0;left:0;width:1200px;height:60px;background:var(--white);z-index:2;display:flex;align-items:center;justify-content:space-between;padding:0 46px}
.brand{font-weight:700;font-size:26px;color:var(--teal);line-height:1;letter-spacing:.3px}
.header-right{display:flex;flex-direction:column;align-items:flex-end;gap:6px}
.top-contact{display:flex;gap:18px;font-size:11px;color:var(--muted)}
.top-contact span{display:flex;align-items:center;gap:5px}
.main-nav{display:flex;gap:0;font-size:12px;font-weight:700;text-transform:uppercase}
.main-nav a{color:var(--ink);text-decoration:none;padding:6px 11px;display:flex;align-items:center}
.main-nav a.home{background:var(--teal);color:var(--white);padding:6px 10px}
.hero{position:absolute;top:60px;left:0;width:1200px;height:560px;background:linear-gradient(180deg,#6d7a8a 0%,#b9a99a 40%,#8a6e52 70%,#3e4a3b 100%)}
.hero-tagline{position:absolute;left:100px;top:450px;display:flex;flex-direction:column;gap:8px}
.hero-tagline span{background:rgba(0,0,0,.82);color:var(--white);font-family:"Roboto Condensed",sans-serif;font-size:25px;font-weight:700;text-transform:uppercase;padding:4px 12px;align-self:flex-start}
.services{position:absolute;top:620px;left:0;width:1200px;height:340px;background:linear-gradient(180deg,var(--teal) 0%,var(--teal-dark) 100%);text-align:center;color:var(--white)}
.services h2{font-size:34px;margin-top:42px}
.services .rule{width:70px;height:2px;background:var(--white);margin:12px auto 0}
.service-list{display:flex;justify-content:center;gap:190px;margin-top:36px}
.service{width:200px;display:flex;flex-direction:column;align-items:center}
.service .circle{width:100px;height:100px;border-radius:50%;background:var(--white);border:4px solid rgba(255,255,255,.5);display:flex;align-items:center;justify-content:center}
.service h3{font-size:20px;margin-top:14px}
.service p{font-size:11px;margin-top:4px;opacity:.9}
.about{position:absolute;top:960px;left:0;width:1200px;height:420px;padding:44px 90px;display:flex;gap:50px}
.about-main{flex:1}
.about-title{font-size:36px;color:var(--teal)}
.about-title b{font-family:"Open Sans",sans-serif;color:var(--teal)}
.about-text{font-size:12.5px;line-height:1.7;color:var(--muted);margin-top:16px}
.pillars{display:flex;gap:40px;margin-top:28px}
.pillar{display:flex;gap:14px;flex:1}
.pillar .dot{width:46px;height:46px;border-radius:50%;background:var(--teal);flex:none;display:flex;align-items:center;justify-content:center}
.pillar h4{font-size:20px}
.pillar p{font-size:11.5px;color:var(--muted);line-height:1.5;margin-top:3px}
.quick-contact{width:300px;flex:none;border:1px solid var(--line);background:var(--white)}
.quick-contact h3{background:var(--teal);color:var(--white);font-size:22px;text-align:center;padding:8px 0}
.qc-body{padding:16px 16px 18px;display:flex;flex-direction:column;gap:9px}
.field{border:1px solid var(--line);height:32px;font-size:12px;color:var(--muted);display:flex;align-items:center;gap:10px;padding:0 10px}
.field.message{height:60px;align-items:flex-start;padding-top:8px}
.submit{background:var(--lime);color:var(--white);font-weight:700;font-size:13px;width:84px;padding:7px 0;text-align:center;margin-top:4px}
.featured{position:absolute;top:1380px;left:0;width:1200px;height:500px;background:var(--light);text-align:center}
.section-title{font-size:36px;color:var(--ink);margin-top:36px}
.section-title em{font-style:normal;color:var(--teal)}
.rule-teal{width:70px;height:2px;background:var(--teal);margin:10px auto 0}
.cards{display:flex;justify-content:center;gap:34px;margin-top:34px}
.card{width:276px;background:var(--white);text-align:left;position:relative}
.card .photo{height:166px;position:relative}
.card .price{position:absolute;right:0;bottom:10px;background:var(--teal);color:var(--white);font-size:12px;font-weight:700;padding:4px 10px}
.card .overlay{position:absolute;inset:0;display:flex;align-items:center;justify-content:center;color:var(--white);font-size:13px;font-weight:600;background:rgba(0,0,0,.35)}
.card .info{padding:12px 14px 10px}
.card h4{font-size:17px;color:var(--teal);font-family:"Roboto Condensed",sans-serif}
.card .county{font-size:12px;color:var(--ink);margin-top:2px}
.card .meta{display:flex;justify-content:flex-start;gap:48px;align-items:center;border-top:1px solid var(--line);margin-top:12px;padding:8px 40px 0 0;font-size:11px;color:var(--muted)}
.card .meta span{display:flex;align-items:center;gap:5px;white-space:nowrap}
.card .next{position:absolute;right:0;bottom:0;width:30px;height:30px;background:var(--teal);display:flex;align-items:center;justify-content:center}
.testimonials{position:absolute;top:1880px;left:0;width:1200px;height:520px;text-align:center}
.testimonials .section-title{margin-top:48px}
.quotes{position:relative;width:900px;margin:40px auto 0;height:320px}
.arrow{position:absolute;top:90px;width:30px;height:30px;display:flex;align-items:center;justify-content:center}
.arrow.prev{left:-140px}.arrow.next{right:-140px}
.quote{position:absolute;width:420px;text-align:left}
.quote .bubble{background:var(--teal);color:var(--white);font-size:13px;font-weight:700;line-height:1.6;padding:22px 24px 22px 46px;position:relative}
.quote .bubble .mark{position:absolute;left:14px;top:8px;font-size:40px;font-family:Georgia,serif;line-height:1}
.quote .bubble::after{content:"";position:absolute;left:54px;bottom:-16px;border-left:16px solid transparent;border-right:16px solid transparent;border-top:16px solid var(--teal)}
.quote.alt .bubble{background:var(--lime)}
.quote.alt .bubble::after{border-top-color:var(--lime)}
.person{display:flex;align-items:center;gap:14px;margin-top:22px;padding-left:24px}
.avatar{width:80px;height:80px;border-radius:50%;border:4px solid var(--white);box-shadow:0 0 0 2px var(--line);background:linear-gradient(160deg,#c8b2a0,#5a4a40)}
.person h5{font-size:17px}
.person small{font-size:12px;color:var(--muted)}
.q1{left:0;top:0}
.q2{left:460px;top:30px}
.newsletter{position:absolute;top:2400px;left:0;width:1200px;height:240px;background:linear-gradient(180deg,#3b4248 0%,#6a737a 55%,#2f6f63 100%)}
.subscribe-box{position:absolute;left:130px;top:30px;width:940px;height:112px;background:var(--white);border-top:4px dashed #d33c3c;display:flex;align-items:center;padding:0 40px;gap:22px}
.subscribe-box .label{display:flex;align-items:center;gap:14px;width:300px}
.subscribe-box .label h3{font-size:24px;color:var(--ink);line-height:1}
.subscribe-box .label p{font-size:15px;color:var(--muted)}
.socials{display:flex;gap:6px}
.socials span{width:24px;height:24px;border-radius:50%;display:block}
.email-input{flex:1;height:36px;border:1px solid var(--line);font-size:12px;color:var(--muted);display:flex;align-items:center;padding:0 12px}
.sub-btn{background:var(--teal);color:var(--white);font-size:13px;font-weight:700;padding:10px 22px}
.site-footer{position:absolute;top:2600px;left:0;width:1200px;height:220px;background:var(--teal);color:var(--white);text-align:center}
.footer-nav{font-size:13px;margin-top:34px;display:flex;justify-content:center;gap:14px}
.footer-contacts{display:flex;justify-content:center;gap:90px;margin-top:34px}
.fc{display:flex;align-items:center;gap:10px;text-align:left;font-size:11px;line-height:1.4}
.fc .ic{width:34px;height:34px;border-radius:50%;border:2px solid var(--white);display:flex;align-items:center;justify-content:center}
.fc strong{font-size:12px}
.copyright{font-size:11px;margin-top:32px;opacity:.85}
</style>
</head>
<body>

<header class="site-header">
  <div class="brand">Marlowe Vane Real Estate</div>
  <div class="header-right">
    <div class="top-contact">
      <span><svg width="12" height="10" viewBox="0 0 12 10"><rect x=".5" y=".5" width="11" height="9" fill="none" stroke="#1fb095"/><path d="M.5 .5 6 5.5 11.5 .5" fill="none" stroke="#1fb095"/></svg>hello@marlowevane.com</span>
      <span><svg width="11" height="11" viewBox="0 0 24 24"><path d="M6.6 10.8a15 15 0 0 0 6.6 6.6l2.2-2.2a1 1 0 0 1 1-.25 11.4 11.4 0 0 0 3.6.6 1 1 0 0 1 1 1V20a1 1 0 0 1-1 1A17 17 0 0 1 3 4a1 1 0 0 1 1-1h3.5a1 1 0 0 1 1 1c0 1.25.2 2.45.6 3.6a1 1 0 0 1-.25 1z" fill="#1fb095"/></svg>555-0142</span>
    </div>
    <nav class="main-nav">
      <a class="home"><svg width="14" height="12" viewBox="0 0 14 12"><path d="M7 0 0 6h2v6h4V8h2v4h4V6h2z" fill="#fff"/></svg></a>
      <a>About Us</a><a>Properties</a><a>Resources</a><a>Testimonials</a><a>Contact Us</a>
    </nav>
  </div>
</header>

<section class="hero" role="img" aria-label="Photograph of a stone luxury home with lit windows, palm trees and a landscaped garden at dusk">
  <div class="hero-tagline">
    <span>We are a brokerage &amp; boutique housing specialist</span>
    <span>with over 27 years of experience in greater Los Angeles area</span>
  </div>
</section>

<section class="services">
  <h2 class="heading">Our Housing Group Offers Assistance And Expertise To</h2>
  <div class="rule"></div>
  <div class="service-list">
    <div class="service">
      <div class="circle"><svg width="52" height="48" viewBox="0 0 52 48"><path d="M26 4 4 22h6v22h32V22h6z" fill="none" stroke="#1fb095" stroke-width="4" stroke-linejoin="round"/><text x="26" y="38" text-anchor="middle" font-size="16" font-weight="700" fill="#1fb095" font-family="Open Sans, sans-serif">$</text></svg></div>
      <h3 class="heading">Home Sellers</h3>
      <p>Pricing guidance and wide market reach</p>
    </div>
    <div class="service">
      <div class="circle"><svg width="52" height="48" viewBox="0 0 52 48"><path d="M26 4 4 22h6v22h32V22h6z" fill="none" stroke="#1fb095" stroke-width="4" stroke-linejoin="round"/><circle cx="26" cy="31" r="5" fill="none" stroke="#1fb095" stroke-width="3"/></svg></div>
      <h3 class="heading">Home Buyers</h3>
      <p>Curated homes in desirable neighborhoods</p>
    </div>
    <div class="service">
      <div class="circle"><svg width="52" height="48" viewBox="0 0 52 48"><path d="M26 4 4 22h6v22h32V22h6z" fill="none" stroke="#1fb095" stroke-width="4" stroke-linejoin="round"/><path d="M18 38l6-7 4 4 6-8" fill="none" stroke="#1fb095" stroke-width="3"/></svg></div>
      <h3 class="heading">Home Investors</h3>
      <p>Sound returns on furnished rentals</p>
    </div>
  </div>
</section>

<section class="about">
  <div class="about-main">
    <h2 class="about-title heading">About <b>Marlowe Vane</b> Real Estate</h2>
    <p class="about-text">We are a Minneapolis brokerage and boutique housing specialist with over 27 years in the furnished housing industry, serving the Greater Los Angeles area. Specializing in warm environments, we offer a customized approach to every guest and client, with a wide array of options in highly desirable areas across the region.</p>
    <div class="pillars">
      <div class="pillar">
        <div class="dot"><svg width="24" height="20" viewBox="0 0 24 20"><circle cx="8" cy="6" r="4" fill="#fff"/><circle cx="17" cy="7" r="3" fill="#fff"/><path d="M0 20c0-5 4-8 8-8s8 3 8 8zM14 20c0-3 1-6 3-7 4 0 7 3 7 7z" fill="#fff"/></svg></div>
        <div><h4 class="heading">Who We Are</h4><p>A local team that treats every home with care and attention.</p></div>
      </div>
      <div class="pillar">
        <div class="dot"><svg width="22" height="22" viewBox="0 0 22 22"><circle cx="11" cy="11" r="9" fill="none" stroke="#fff" stroke-width="2.5"/><circle cx="11" cy="11" r="4" fill="#fff"/></svg></div>
        <div><h4 class="heading">Our Mission</h4><p>To match each client with a warm home in the right neighborhood.</p></div>
      </div>
    </div>
  </div>
  <aside class="quick-contact">
    <h3 class="heading">Quick Contact</h3>
    <div class="qc-body">
      <div class="field"><svg width="12" height="12" viewBox="0 0 12 12"><circle cx="6" cy="3.5" r="3" fill="#1fb095"/><path d="M0 12c0-4 3-5 6-5s6 1 6 5z" fill="#1fb095"/></svg>Name</div>
      <div class="field"><svg width="12" height="10" viewBox="0 0 12 10"><rect x=".5" y=".5" width="11" height="9" fill="none" stroke="#1fb095"/><path d="M.5 .5 6 5.5 11.5 .5" fill="none" stroke="#1fb095"/></svg>Email</div>
      <div class="field"><svg width="12" height="12" viewBox="0 0 24 24"><path d="M6.6 10.8a15 15 0 0 0 6.6 6.6l2.2-2.2a1 1 0 0 1 1-.25 11.4 11.4 0 0 0 3.6.6 1 1 0 0 1 1 1V20a1 1 0 0 1-1 1A17 17 0 0 1 3 4a1 1 0 0 1 1-1h3.5a1 1 0 0 1 1 1c0 1.25.2 2.45.6 3.6a1 1 0 0 1-.25 1z" fill="#1fb095"/></svg>Phone</div>
      <div class="field message"><svg width="12" height="12" viewBox="0 0 12 12"><path d="M1 1h10v7H5l-3 3V8H1z" fill="#1fb095"/></svg>Message</div>
      <div class="submit">SUBMIT</div>
    </div>
  </aside>
</section>

<section class="featured">
  <h2 class="section-title heading"><span>Featured</span> <em>Properties</em></h2>
  <div class="rule-teal"></div>
  <div class="cards">
    <article class="card">
      <div class="photo" role="img" aria-label="Photograph of a modern living room with a view onto a garden" style="background:linear-gradient(160deg,#c7b89a,#6e5a44)"><span class="price">$ 1,495,000</span></div>
      <div class="info"><h4>26600 Laurel Canyon Dr</h4><div class="county">Los Angeles County</div>
        <div class="meta"><span>&#9673; View Details</span><span>&#9635; Photos</span></div></div>
      <div class="next"><svg width="10" height="12" viewBox="0 0 10 12"><path d="M2 1l6 5-6 5" fill="none" stroke="#fff" stroke-width="2"/></svg></div>
    </article>
    <article class="card">
      <div class="photo" role="img" aria-label="Photograph of a bright open-plan interior with a dining area" style="background:linear-gradient(160deg,#a79a8c,#4a4038)"><div class="overlay">See all property listings</div><span class="price">$ 1,495,000</span></div>
      <div class="info"><h4>26600 Laurel Canyon Dr</h4><div class="county">Los Angeles County</div>
        <div class="meta"><span>&#9673; View Details</span><span>&#9635; Photos</span></div></div>
      <div class="next"><svg width="10" height="12" viewBox="0 0 10 12"><path d="M2 1l6 5-6 5" fill="none" stroke="#fff" stroke-width="2"/></svg></div>
    </article>
    <article class="card">
      <div class="photo" role="img" aria-label="Photograph of an elegant furnished living room in warm tones" style="background:linear-gradient(160deg,#b58a62,#5b3a24)"><span class="price">$ 1,495,000</span></div>
      <div class="info"><h4>26600 Laurel Canyon Dr</h4><div class="county">Los Angeles County</div>
        <div class="meta"><span>&#9673; View Details</span><span>&#9635; Photos</span></div></div>
      <div class="next"><svg width="10" height="12" viewBox="0 0 10 12"><path d="M2 1l6 5-6 5" fill="none" stroke="#fff" stroke-width="2"/></svg></div>
    </article>
  </div>
</section>

<section class="testimonials">
  <h2 class="section-title heading"><em>Client</em> Testimonials</h2>
  <div class="rule-teal"></div>
  <div class="quotes">
    <div class="arrow prev"><svg width="12" height="20" viewBox="0 0 12 20"><path d="M10 2 2 10l8 8" fill="none" stroke="#9aa2a7" stroke-width="2.5"/></svg></div>
    <div class="arrow next"><svg width="12" height="20" viewBox="0 0 12 20"><path d="M2 2l8 8-8 8" fill="none" stroke="#9aa2a7" stroke-width="2.5"/></svg></div>
    <div class="quote q1">
      <div class="bubble"><span class="mark">&ldquo;</span>They found us a warm, furnished home in days and handled every detail with real care.</div>
      <div class="person"><div class="avatar" role="img" aria-label="Portrait photo of the client"></div><div><h5 class="heading">Daniel Ashford</h5><small>Customer</small></div></div>
    </div>
    <div class="quote q2 alt">
      <div class="bubble"><span class="mark">&ldquo;</span>Smooth purchase, honest advice and a team that truly listens to what buyers need.</div>
      <div class="person"><div class="avatar" role="img" aria-label="Portrait photo of the client"></div><div><h5 class="heading">Clara Whitfield</h5><small>Customer</small></div></div>
    </div>
  </div>
</section>

<section class="newsletter" role="img" aria-label="Photograph of a city skyline with palm trees">
  <div class="subscribe-box">
    <div class="label">
      <svg width="46" height="36" viewBox="0 0 46 36"><rect x="1.5" y="1.5" width="43" height="33" fill="none" stroke="#333a3f" stroke-width="3"/><path d="M1.5 1.5 23 20 44.5 1.5" fill="none" stroke="#333a3f" stroke-width="3"/></svg>
      <div><h3 class="heading">SUBSCRIBE</h3><p>for Latest News</p></div>
    </div>
    <div class="socials"><span style="background:#3b5b98"></span><span style="background:#2fa9e0"></span><span style="background:#d8432f"></span></div>
    <div class="email-input">Enter Email Address</div>
    <div class="sub-btn">SUBSCRIBE</div>
  </div>
</section>

<footer class="site-footer">
  <nav class="footer-nav"><span>Home</span><span>/</span><span>About Us</span><span>/</span><span>Properties</span><span>/</span><span>Resources</span><span>/</span><span>Testimonials</span><span>/</span><span>Contact Us</span></nav>
  <div class="footer-contacts">
    <div class="fc"><div class="ic"><svg width="12" height="16" viewBox="0 0 12 16"><path d="M6 0a6 6 0 0 0-6 6c0 4.5 6 10 6 10s6-5.5 6-10a6 6 0 0 0-6-6z" fill="#fff"/><circle cx="6" cy="6" r="2" fill="#1fb095"/></svg></div><div><strong>Marlowe Vane Real Estate</strong><br>1820 Harbor View Blvd, Los Angeles CA</div></div>
    <div class="fc"><div class="ic"><svg width="14" height="14" viewBox="0 0 24 24"><path d="M6.6 10.8a15 15 0 0 0 6.6 6.6l2.2-2.2a1 1 0 0 1 1-.25 11.4 11.4 0 0 0 3.6.6 1 1 0 0 1 1 1V20a1 1 0 0 1-1 1A17 17 0 0 1 3 4a1 1 0 0 1 1-1h3.5a1 1 0 0 1 1 1c0 1.25.2 2.45.6 3.6a1 1 0 0 1-.25 1z" fill="#fff"/></svg></div><div><strong>Call Us</strong><br>555-0142</div></div>
    <div class="fc"><div class="ic"><svg width="14" height="11" viewBox="0 0 12 10"><rect x=".5" y=".5" width="11" height="9" fill="none" stroke="#fff"/><path d="M.5 .5 6 5.5 11.5 .5" fill="none" stroke="#fff"/></svg></div><div><strong>Email Us</strong><br>hello@marlowevane.com</div></div>
  </div>
  <p class="copyright">Copyright &copy; 2024 Marlowe Vane Real Estate. All Rights Reserved.</p>
</footer>

</body>
</html>
```